Website for Arts Studios including Audio, Video and Performing Arts

Creating an engaging and informative website for Brightwell Studios is a paramount endeavor that demands careful consideration of the brand's identity, values, and goals. This project offers a unique opportunity to showcase the studio's multifaceted offerings and establish a strong online presence. In order to fulfill the objectives outlined in the website brief, we will design a comprehensive, user-friendly, and aesthetically pleasing website that not only introduces Brightwell Studios to the world but also provides a seamless experience for visitors.

The website's primary focus is to present Brightwell Studios as a hub for creativity, wellness, and community engagement. To achieve this, we will construct various sections that highlight the studio's features and appeal to a broad audience:

1. **Classes and Studio Sessions**: A central element of the website will be dedicated to showcasing the various classes and studio sessions offered by Brightwell Studios. This section will provide detailed information about the classes available, their schedules, and the instructors, encouraging visitors to explore and sign up for sessions that align with their interests and needs.

2. **About Section**: This segment will provide an in-depth insight into the ethos and history of Brightwell Studios. It will introduce the founders, their vision, and the core values that underpin the studio's operations. We will incorporate compelling storytelling and visuals to create a strong emotional connection with visitors.

3. **Staffing Section**: Highlighting the talented and dedicated team behind Brightwell Studios is crucial. This section will include profiles of instructors, trainers, and support staff, enabling visitors to get to know the individuals who make the studio a vibrant and welcoming place.

4. **Phases Description**: To communicate the studio's growth and evolution, we will incorporate a section outlining the different phases of development. Phase 1, Phase 2, and future phases will be described, giving visitors a clear understanding of Brightwell Studios' ongoing commitment to innovation and expansion.

5. **Contact Us**: A user-friendly contact section will be integrated to facilitate easy communication between Brightwell Studios and its audience. Visitors can inquire about classes, studio bookings, or any other inquiries, fostering a sense of accessibility and approachability.

In addition to these core sections, the website will also prioritize responsive design and easy navigation, ensuring that users can access the information they seek on various devices and screen sizes. We will focus on creating a visually appealing and cohesive design, using a color palette and imagery that aligns with the studio's branding.

In conclusion, the website we propose for Brightwell Studios goes beyond being a mere online presence; it serves as a dynamic platform to introduce the studio to the world. By combining compelling content, user-friendly features, and a commitment to capturing the essence of Brightwell Studios, our design will help the studio engage with a global audience, promote its mission, and foster a sense of belonging among its visitors.

Target Market(s)

Artists in the DFW metroplec

Industry/Entity Type

Entertainment/Music/Performing Arts

Coding

Coded - Design and coding required

Number of Pages Required

1 page

Font styles to use
Other font styles liked:
• Cachet should be included within the font set.

Colors
FFC000
F8CF3A
FAE287
FDF2CF
FEFAEE

Requirements
Must have
• The sections in the description
Nice to have
• A floating video in the background of the landing page
Should not have
• any ecommerce bits

```html
<!DOCTYPE html>
<html lang="en">
<head>
<meta charset="utf-8">
<title>Brightwell Studios</title>
<link href="https://fonts.googleapis.com/css2?family=Oswald:wght@300;400;500;600&family=Lato:wght@400;700&display=swap" rel="stylesheet">
<style>
:root{
  --ink:#0d0d0d;
  --dark:#141414;
  --white:#ffffff;
  --text:#222222;
  --muted:#3a3a3a;
  --gold:#ffc000;
  --amber:#f8cf3a;
  --line:#3a3a3a;
}
*{margin:0;padding:0;box-sizing:border-box}
html,body{width:1200px;height:3824px;overflow:hidden}
body{position:relative;background:var(--white);font-family:'Lato',sans-serif;color:var(--text)}
.abs{position:absolute}
.bg-shape{position:absolute;left:0;width:1200px}
.head{font-family:'Oswald',sans-serif;text-transform:uppercase}
.center{left:0;width:1200px;text-align:center}

/* header */
.logo{left:111px;top:30px;font-family:'Oswald',sans-serif;font-size:26px;color:var(--white);font-weight:400}
.nav{left:497px;top:36px;display:flex;gap:36px;font-family:'Oswald',sans-serif;font-size:14px;color:var(--white);text-transform:uppercase}
.nav-cta{left:985px;top:28px;width:104px;height:37px;background:var(--white);color:var(--ink);font-family:'Oswald',sans-serif;font-size:14px;display:flex;align-items:center;justify-content:center;text-transform:uppercase}
.header-rule{left:111px;top:98px;width:978px;height:1px;background:var(--line)}
.welcome{top:142px;font-family:'Oswald',sans-serif;font-size:54px;color:transparent;-webkit-text-stroke:1px #8a8a8a;text-transform:uppercase;letter-spacing:1px}
.hero-title{top:215px;font-family:'Oswald',sans-serif;font-size:70px;color:var(--white);letter-spacing:17px;font-weight:500}
.video{left:111px;top:368px;width:978px;height:490px;border:3px solid var(--white);background:radial-gradient(ellipse at 50% 85%,#6b4412 0%,#2e1c08 40%,#120b04 80%),linear-gradient(90deg,#3d2609,#1a1005 50%,#3d2609)}
.play{left:570px;top:555px;width:60px;height:60px;border-radius:50%;background:var(--white);box-shadow:0 0 0 6px rgba(255,255,255,.25);display:flex;align-items:center;justify-content:center}

/* classes */
.section-title{font-family:'Oswald',sans-serif;font-size:46px;font-weight:500;color:var(--ink);text-transform:uppercase}
.class-photo{top:1014px;height:449px}
.class-card{left:401px;top:1014px;width:398px;height:449px;background:var(--white);box-shadow:0 2px 12px rgba(0,0,0,.18);border-bottom:3px solid var(--ink)}
.class-card-photo{left:15px;top:17px;width:370px;height:249px;background:linear-gradient(135deg,#7a4a1e,#2a1a12 55%,#3b5470)}
.class-card-tab{left:30px;top:242px;width:340px;height:24px;background:var(--white)}
.class-name{top:250px;width:398px;text-align:center;font-family:'Oswald',sans-serif;font-size:16px;font-weight:500;color:var(--ink)}
.class-desc{top:278px;left:40px;width:318px;text-align:center;font-size:11px;line-height:21px;color:var(--muted)}
.class-meta{width:398px;text-align:center}
.btn-dark{background:var(--ink);color:var(--white);font-family:'Oswald',sans-serif;display:flex;align-items:center;justify-content:center;text-transform:uppercase}
.arrow{width:36px;height:36px;border-radius:50%;background:var(--ink);display:flex;align-items:center;justify-content:center}

/* about */
.about-intro{left:170px;top:1616px;width:860px;text-align:center;font-size:15px;line-height:29.5px;color:var(--muted)}
.portrait{left:111px;top:1737px;width:468px;height:580px;background:var(--white);box-shadow:0 2px 10px rgba(0,0,0,.3);padding:5px}
.portrait-fill{width:100%;height:100%;background:linear-gradient(160deg,#3c4650,#1f2a33 50%,#2e3338)}
.about-col{left:655px;width:434px}
.about-head{font-family:'Oswald',sans-serif;font-size:32px;color:var(--ink);text-transform:uppercase;font-weight:400}
.about-text{font-size:14px;line-height:31.5px;color:var(--muted);margin-top:8px}
.about-text.tight{line-height:29.5px}

/* bookings */
.booking-title{top:2478px;font-family:'Oswald',sans-serif;font-size:46px;font-weight:500;color:var(--white);text-transform:uppercase}
.booking-text{left:200px;top:2557px;width:800px;text-align:center;font-size:15px;line-height:32px;color:var(--white)}
.btn-light{left:530px;top:2676px;width:140px;height:52px;background:var(--white);color:var(--ink);font-family:'Oswald',sans-serif;font-size:17px;display:flex;align-items:center;justify-content:center;text-transform:uppercase}

/* staffing */
.staff-card{top:3037px;width:293px;height:294px;background:var(--white);box-shadow:0 2px 12px rgba(0,0,0,.15)}
.staff-photo{top:2983px;width:266px;height:281px}
.staff-label{left:0;top:3284px;width:293px;text-align:center;font-family:'Oswald',sans-serif;font-size:21px;font-weight:500;color:var(--ink);text-transform:uppercase;line-height:30px}

/* footer */
.footer{left:0;top:3414px;width:1200px;height:410px;background:var(--dark)}
.footer-logo{left:111px;top:3488px;font-family:'Oswald',sans-serif;font-size:32px;color:var(--white)}
.social{top:3567px;width:32px;height:32px;border-radius:50%;background:var(--white)}
.footer-head{top:3487px;font-family:'Oswald',sans-serif;font-size:20px;color:var(--white);text-transform:uppercase}
.footer-list{list-style:none;font-size:15px;color:var(--white)}
.footer-list li{height:34px;display:flex;align-items:center;gap:10px}
.contact-row{left:897px;display:flex;gap:14px;align-items:flex-start;font-size:15px;line-height:27px;color:var(--white)}
.contact-icon{width:30px;height:30px;border-radius:50%;background:var(--white);display:flex;align-items:center;justify-content:center;flex:none}
.footer-rule{left:111px;top:3738px;width:978px;height:1px;background:#555}
.copyright{top:3772px;font-size:15px;font-weight:700;color:var(--white)}
</style>
</head>
<body>

<!-- hero background -->
<svg class="bg-shape" style="top:0" width="1200" height="770" viewBox="0 0 1200 770">
  <defs>
    <linearGradient id="heroShade" x1="0" y1="0" x2="1" y2="1">
      <stop offset="0" stop-color="#1b1b1b"/>
      <stop offset="0.5" stop-color="#0b0b0b"/>
      <stop offset="1" stop-color="#1d1d1d"/>
    </linearGradient>
  </defs>
  <polygon points="0,0 1200,0 1200,569 0,765" fill="url(#heroShade)"/>
</svg>

<header>
  <div class="abs logo">BRIGHTWELL STUDIOS</div>
  <nav class="abs nav">
    <span>Home</span><span>Classes and Studio</span><span>About</span><span>Staffing</span><span>Phases</span>
  </nav>
  <div class="abs nav-cta">Contact Us</div>
  <div class="abs header-rule"></div>
</header>

<section class="hero">
  <div class="abs center welcome">Welcome To</div>
  <h1 class="abs center hero-title">BRIGHTWELL STUDIOS</h1>
  <div class="abs video" role="img" aria-label="Video still of a glowing golden stage with light columns"></div>
  <div class="abs play">
    <svg width="22" height="24" viewBox="0 0 22 24"><polygon points="3,1 21,12 3,23" fill="#111"/></svg>
  </div>
</section>

<section class="classes">
  <h2 class="abs center section-title" style="top:915px">Classes and Studio Sessions</h2>
  <div class="abs class-photo" style="left:111px;width:268px;background:linear-gradient(120deg,#1a1a1a,#d9d9d9 45%,#2b2b2b);border-bottom:3px solid var(--ink)" role="img" aria-label="Photographer setting up a white studio backdrop"></div>
  <div class="abs class-card">
    <div class="abs class-card-photo" role="img" aria-label="Editor working at a video editing desk"></div>
    <div class="abs class-card-tab"></div>
    <div class="abs class-name">NAME 2</div>
    <p class="abs class-desc">Itaque earum rerum hic tenetur a sapiente delectus, ut aut voluptatibus maiores alias consequatur</p>
    <div class="abs class-meta head" style="top:330px;font-size:15px;font-weight:500;color:var(--ink)">Instructor: Sapiente</div>
    <div class="abs class-meta" style="top:362px;font-size:13px;color:var(--muted)">DATE: 10 NOV 2023, TIME: 10.00 AM</div>
    <div class="abs btn-dark" style="left:153px;top:394px;width:92px;height:30px;font-size:13px">Sign Up</div>
  </div>
  <div class="abs class-photo" style="left:821px;width:268px;background:radial-gradient(ellipse at 55% 45%,#5a1a1a,#1a0808 55%,#0a0a0a)" role="img" aria-label="Performer in a dark dress on stage"></div>
  <div class="abs arrow" style="left:35px;top:1219px">
    <svg width="14" height="14" viewBox="0 0 14 14"><polyline points="9,2 4,7 9,12" fill="none" stroke="#fff" stroke-width="2.4"/></svg>
  </div>
  <div class="abs arrow" style="left:1115px;top:1219px">
    <svg width="14" height="14" viewBox="0 0 14 14"><polyline points="5,2 10,7 5,12" fill="none" stroke="#fff" stroke-width="2.4"/></svg>
  </div>
</section>

<section class="about">
  <h2 class="abs center section-title" style="top:1544px">About Brightwell Studios</h2>
  <p class="abs about-intro">Temporibus autem quibusdam et aut officiis debitis aut rerum necessitatibus saepe eveniet ut et voluptates repudiandae sint et molestiae non recusandae. Itaque earum rerum hic tenetur a sapiente delectus, ut aut reiciendis voluptatibus maiores alias consequatur aut perferendis doloribus asperiores repellat.</p>
  <div class="abs portrait"><div class="portrait-fill" role="img" aria-label="Portrait of the studio founder in an office"></div></div>
  <div class="abs about-col" style="top:1726px">
    <h3 class="about-head" style="font-weight:500">Marlon Reyes</h3>
    <p class="about-text">At vero eos et accusamus et iusto odio dignissimos ducimus qui blanditiis praesentium voluptatum deleniti atque corrupti quos dolores et quas molestias excepturi sint occaecati cupiditate non provident, similique sunt in culpa qui officia deserunt mollitia animi, id est laborum et dolorum fuga.</p>
  </div>
  <div class="abs about-col" style="top:1956px">
    <h3 class="about-head">Vision</h3>
    <p class="about-text tight">Nam libero tempore, cum soluta nobis est eligendi optio cumque nihil impedit quo minus id quod maxime placeat facere possimus, omnis voluptas assumenda est, omnis dolor repellendus.</p>
  </div>
  <div class="abs about-col" style="top:2103px">
    <h3 class="about-head">Core Values</h3>
    <p class="about-text tight">Temporibus autem quibusdam et aut officiis debitis aut rerum necessitatibus saepe eveniet ut et voluptates repudiandae sint etofficiis debitis molestia.</p>
  </div>
  <div class="abs btn-dark" style="left:655px;top:2257px;width:140px;height:52px;font-size:16px">Read More</div>
</section>

<section class="bookings">
  <svg class="bg-shape" style="top:2345px" width="1200" height="530" viewBox="0 0 1200 530" role="img" aria-label="Dark stage backdrop with a dancer silhouette">
    <defs>
      <radialGradient id="bookShade" cx="0.5" cy="0.4" r="0.6">
        <stop offset="0" stop-color="#3a3a3a"/>
        <stop offset="1" stop-color="#080808"/>
      </radialGradient>
    </defs>
    <polygon points="0,105 1200,4 1200,426 0,525" fill="url(#bookShade)"/>
  </svg>
  <h2 class="abs center booking-title">Studio Bookings</h2>
  <p class="abs booking-text">Itaque earum rerum hic tenetur a sapiente delectus, ut aut reiciendis voluptatibus maiores alias consequatur aut perferendis doloribus asperiores repellat.Temporibus autem quibusdam et aut officiis debitis aut rerum necessitatibus saepe eveniet ut et voluptates repudiandae sint et molestiae non recusandae.</p>
  <div class="abs btn-light">Book Now</div>
</section>

<section class="staffing">
  <h2 class="abs center section-title" style="top:2880px">Our Staffing</h2>
  <div class="abs staff-card" style="left:111px"></div>
  <div class="abs staff-card" style="left:453px"></div>
  <div class="abs staff-card" style="left:796px"></div>
  <div class="abs staff-photo" style="left:125px;background:linear-gradient(180deg,#c8ccd0,#3d5a6e 55%,#2a2f35)" role="img" aria-label="Instructor lecturing to a full auditorium"></div>
  <div class="abs staff-photo" style="left:467px;background:linear-gradient(180deg,#4a4f55,#1e2a44 60%,#d8d8d8)" role="img" aria-label="Trainer in a suit seated at a desk"></div>
  <div class="abs staff-photo" style="left:809px;background:linear-gradient(180deg,#b9a58e,#6b7258 60%,#8a8a8a)" role="img" aria-label="Support staff member with a headset at a laptop"></div>
  <div class="abs staff-label" style="left:111px">Instructors</div>
  <div class="abs staff-label" style="left:453px">Trainers</div>
  <div class="abs staff-label" style="left:796px">Support Staff</div>
</section>

<footer>
  <div class="abs footer"></div>
  <div class="abs footer-logo">BRIGHTWELL STUDIOS</div>
  <div class="abs social" style="left:111px"></div>
  <div class="abs social" style="left:168px"></div>
  <div class="abs social" style="left:226px"></div>
  <div class="abs social" style="left:283px"></div>

  <div class="abs footer-head" style="left:429px">Quick Link</div>
  <ul class="abs footer-list" style="left:429px;top:3526px">
    <li><svg width="14" height="12" viewBox="0 0 14 12"><path d="M1 6h11M7 1l5 5-5 5" fill="none" stroke="#fff" stroke-width="2"/></svg>Home</li>
    <li><svg width="14" height="12" viewBox="0 0 14 12"><path d="M1 6h11M7 1l5 5-5 5" fill="none" stroke="#fff" stroke-width="2"/></svg>About</li>
    <li><svg width="14" height="12" viewBox="0 0 14 12"><path d="M1 6h11M7 1l5 5-5 5" fill="none" stroke="#fff" stroke-width="2"/></svg>Classes and Studio</li>
    <li><svg width="14" height="12" viewBox="0 0 14 12"><path d="M1 6h11M7 1l5 5-5 5" fill="none" stroke="#fff" stroke-width="2"/></svg>Staffing</li>
    <li><svg width="14" height="12" viewBox="0 0 14 12"><path d="M1 6h11M7 1l5 5-5 5" fill="none" stroke="#fff" stroke-width="2"/></svg>Contact Us</li>
  </ul>

  <div class="abs footer-head" style="left:661px">Help Links</div>
  <ul class="abs footer-list" style="left:661px;top:3526px">
    <li><svg width="14" height="12" viewBox="0 0 14 12"><path d="M1 6h11M7 1l5 5-5 5" fill="none" stroke="#fff" stroke-width="2"/></svg>FAQ</li>
    <li><svg width="14" height="12" viewBox="0 0 14 12"><path d="M1 6h11M7 1l5 5-5 5" fill="none" stroke="#fff" stroke-width="2"/></svg>Terms of use</li>
    <li><svg width="14" height="12" viewBox="0 0 14 12"><path d="M1 6h11M7 1l5 5-5 5" fill="none" stroke="#fff" stroke-width="2"/></svg>Privacy Policy</li>
    <li><svg width="14" height="12" viewBox="0 0 14 12"><path d="M1 6h11M7 1l5 5-5 5" fill="none" stroke="#fff" stroke-width="2"/></svg>Support Links</li>
    <li><svg width="14" height="12" viewBox="0 0 14 12"><path d="M1 6h11M7 1l5 5-5 5" fill="none" stroke="#fff" stroke-width="2"/></svg>Conditions</li>
  </ul>

  <div class="abs footer-head" style="left:897px">Contact Us</div>
  <div class="abs contact-row" style="top:3534px">
    <span class="contact-icon"><svg width="14" height="18" viewBox="0 0 14 18"><path d="M7 1a6 6 0 0 0-6 6c0 4.5 6 10 6 10s6-5.5 6-10a6 6 0 0 0-6-6z" fill="#111"/><circle cx="7" cy="7" r="2.2" fill="#fff"/></svg></span>
    <span>Brightwell Studios<br>United States</span>
  </div>
  <div class="abs contact-row" style="top:3601px">
    <span class="contact-icon"><svg width="16" height="16" viewBox="0 0 16 16"><path d="M3 1l3 3-1.5 2a9 9 0 0 0 5.5 5.5L12 10l3 3-2 2C7 15 1 9 1 3z" fill="#111"/></svg></span>
    <span style="line-height:30px">+1 214 555 0142</span>
  </div>
  <div class="abs contact-row" style="top:3652px">
    <span class="contact-icon"><svg width="16" height="12" viewBox="0 0 16 12"><rect x="1" y="1" width="14" height="10" rx="1" fill="#111"/><path d="M1 2l7 5 7-5" fill="none" stroke="#fff" stroke-width="1.2"/></svg></span>
    <span style="line-height:30px">info@brightwellstudios.com</span>
  </div>

  <div class="abs footer-rule"></div>
  <div class="abs center copyright">Copyrights@2023.Brightwell Studios.All Rights Reserved</div>
</footer>

</body>
</html>
```